"Dario Quillon" Business Card

Friends

My name is "Dario Quillon" and I need your help! I need a new business card for my personal use.

As background, "Dario Quillon" is actually an alias that I use when I meet women. Please use your creative skills to create an amazing business card for me to use!

In addition to including my name and contact details (see the "Must Have" section), you may wish to add a catchphrase or a title if you think it would help me :)

For background, please see:

http://www.dailybrightwire.com/2013/07/23/morton-feld-dario-quillon_n_5129847.html

Looking forward to seeing what you can do for me.

Hugs and kisses,

Dario Quillon [courtesy of PixelHarbor]

Target Market(s)

Adult women in New York City...or anywhere really.

Industry/Entity Type

Business

Requirements
Must have
• Please include the following details:

Dario Quillon
P: +1-555-3QUILLN
E: secrets@darioquillon-mail.com
Nice to have
• You might include a catchphrase, like "Quillon is my surname But you can call me Mr Smoothstep".

Or perhaps a title, like "Dario Quillon, Head of Sexy Times".

You're creative...I will leave the details to you my friends.
Should not have
• Any references to my actual name...because then, what's the point in using an alias?

```html
<!DOCTYPE html>
<html lang="en">
<head>
<meta charset="utf-8">
<title>Dario Quillon — Business Card</title>
<link rel="stylesheet" href="https://fonts.googleapis.com/css2?family=Poiret+One&display=swap">
<style>
  :root {
    --stage: #1e1e1e;
    --card: #2e2e2e;
    --card-edge: #262626;
    --name-blue: #5ba8e8;
    --tag-pink: #c4338c;
    --icon-bg: #8a8a8a;
    --icon-fg: #2e2e2e;
    --contact-white: #e6e6e6;
  }
  * { margin: 0; padding: 0; box-sizing: border-box; }
  html, body {
    width: 1200px;
    height: 791px;
    overflow: hidden;
    background: var(--stage);
  }
  .stage {
    position: relative;
    width: 1200px;
    height: 791px;
  }
  .card {
    position: absolute;
    top: 247px;
    width: 520px;
    height: 297px;
    background: var(--card);
    border: 1px solid var(--card-edge);
    font-family: "Poiret One", sans-serif;
    overflow: hidden;
  }
  .card--front { left: 50px; }
  .card--back { left: 630px; }
  .card__texture {
    position: absolute;
    inset: 0;
    background: linear-gradient(160deg, #313131, #2a2a2a);
  }
  .card__content {
    position: relative;
    height: 100%;
    display: flex;
    flex-direction: column;
    align-items: center;
  }
  .card--front .card__content { padding-top: 52px; }
  .card--back .card__content { padding-top: 92px; }
  .brand-name {
    display: flex;
    align-items: center;
    gap: 14px;
    color: var(--name-blue);
    font-size: 44px;
    line-height: 1;
    letter-spacing: 0.5px;
  }
  .brand-name__dot {
    width: 14px;
    height: 14px;
    border-radius: 50%;
    background: var(--tag-pink);
  }
  .tagline {
    margin-top: 18px;
    color: var(--tag-pink);
    font-size: 24px;
    text-decoration: underline;
    text-underline-offset: 4px;
    text-decoration-thickness: 1px;
  }
  .contact {
    margin-top: 38px;
    display: flex;
    flex-direction: column;
    gap: 10px;
    align-items: center;
  }
  .contact__row {
    display: flex;
    align-items: center;
    gap: 10px;
    font-size: 22px;
  }
  .contact__row--phone { color: var(--contact-white); }
  .contact__row--email { color: var(--tag-pink); }
  .contact__icon {
    width: 20px;
    height: 20px;
    display: block;
  }
</style>
</head>
<body>
<main class="stage">

  <section class="card card--front" aria-label="Business card front">
    <div class="card__texture" role="img" aria-label="Fine triangular grid pattern over dark grey card stock"></div>
    <div class="card__content">
      <h1 class="brand-name">Dario <span class="brand-name__dot"></span> Quillon</h1>
      <p class="tagline">and the sexy times begin</p>
      <div class="contact">
        <p class="contact__row contact__row--phone">
          <svg class="contact__icon" viewBox="0 0 20 20" aria-hidden="true">
            <rect width="20" height="20" rx="3" fill="var(--icon-bg)"/>
            <path d="M6 4.5c-1 1-1.2 2.6 0 4.6 1.3 2.2 3.1 4.1 5.3 5.3 1.9 1.1 3.4.9 4.3-.1l-2.1-2.1-1.6 1c-1.6-.8-2.9-2.1-3.7-3.7l1-1.6L7 4.5z" fill="var(--icon-fg)"/>
          </svg>
          +1-555-3QUILLN
        </p>
        <p class="contact__row contact__row--email">
          secrets@darioquillon-mail.com
          <svg class="contact__icon" viewBox="0 0 20 20" aria-hidden="true">
            <rect width="20" height="20" rx="3" fill="var(--icon-bg)"/>
            <rect x="4" y="6" width="12" height="8.5" fill="none" stroke="var(--icon-fg)" stroke-width="1.4"/>
            <path d="M4 6l6 5 6-5" fill="none" stroke="var(--icon-fg)" stroke-width="1.4"/>
          </svg>
        </p>
      </div>
    </div>
  </section>

  <section class="card card--back" aria-label="Business card back">
    <div class="card__texture" role="img" aria-label="Fine triangular grid pattern over dark grey card stock"></div>
    <div class="card__content">
      <h2 class="brand-name">Dario <span class="brand-name__dot"></span> Quillon</h2>
      <p class="tagline">and the sexy times begin</p>
    </div>
  </section>

</main>
</body>
</html>
```